CoinLantern one-page corporate website

Our company, CoinLantern is a cryptocurrency Initial Coin Offering ("ICO" marketing and promotion agency, which requires a professional company landing page design whereby prospective clients can learn;
-who we are
-what we do
-what our people are saying about us
-core team members
-subscribe to our mailing list
-how to get in touch (basic contact form)

We are looking for something unique and attractive -- not a standard Pako template that we could put together ourselves. Plain stock images should not be used. Unique visualizations of the service offerings and creative presentation are key. We are a cutting edge marketing agency and as such, we need to look the part.

Relevant documentation about the business and branding assets have been attached to guide the designer. Certain information will be included by the company at a later date such as team member descriptions. As such, lorem ipsum may be included wherever necessary to help visualize the textual areas.

****Please ensure that you actually utilize the photos and graphics provided so that we can have a good picture of what it would actually look like with our branding.

The site must be responsive HTML CSS Design.

Sites style themes we like for inspiration and specific sections we like ****Very important***:
https://vaultorbitra.example/offers - we like that the token & company logo is used in unique visualizations that connects various ideas together. We imagine unique visuals such as these with our Icon (see attached) serving as a token. We also like the unique and attractive visual theme of the webpage itself.

https://quarrelstone.example/ - we like the layout of this website, specifically how the service offerings are displayed in a circular visual graphic with the Quarrel logo in the middle. We imagine a similar type of graphic designed with CoinLantern in the middle.

https://zorvinet.example/ - we like how the logo is central to the theme in this site when you first enter and how it fades + shrinks into the distance as you scroll down.

Target Market(s)

cryptocurrency entrepreneurs and ICOs

Industry/Entity Type

It Company

Coding

Coded - Design and coding required

Number of Pages Required

1 page

Font styles to use
Sans Serif

Colors

Designer to choose colors to be used in the design.

Requirements
Must have
• The site must be responsive HTML CSS Design.
• The page must be modern and visually attractive. Elements must not be static and should have a fluid motion / visual change as the user scrolls through the page.
Should not have
• The project should not use any old stock images or elements which are dull and over-used, but rather images or elements should be unique and well thought out.

```html
<!DOCTYPE html>
<html lang="en">
<head>
<meta charset="utf-8">
<title>CoinLantern — The Token Sale Experts</title>
<link rel="stylesheet" href="https://fonts.googleapis.com/css2?family=Raleway:ital,wght@0,400;0,500;0,600;0,700;0,800;1,400;1,600&display=swap">
<style>
:root{
  --blue:#1b9bd8;
  --blue-bright:#21a9e8;
  --navy:#1d3f6b;
  --navy-deep:#14325a;
  --ink:#27415f;
  --text:#5a6472;
  --muted:#8b949f;
  --line:#2aa6df;
  --field:#eceef1;
  --white:#ffffff;
  --mist:#eef1f4;
}
*{box-sizing:border-box;margin:0;padding:0}
html,body{width:1200px;height:5248px;overflow:hidden}
body{font-family:"Raleway",sans-serif;color:var(--text);background:var(--white);position:relative}
.section{position:absolute;left:0;width:1200px}

/* headings */
.section-title{display:flex;align-items:center;justify-content:center;gap:14px;font-size:40px;font-weight:700;color:var(--ink)}
.section-title .accent{color:var(--blue);font-weight:500}
.title-dot{width:34px;height:34px;border-radius:50%;border:3px solid var(--blue);flex:none}

/* hero */
.hero{top:0;height:760px;background:linear-gradient(180deg,#0d3d78 0%,#1467b0 45%,#2a8fd6 75%,#7cc3ec 100%);overflow:hidden}
.menu{position:absolute;right:36px;top:18px;width:40px}
.menu span{display:block;height:4px;background:var(--white);margin-bottom:7px;border-radius:2px}
.brand{position:absolute;top:180px;left:0;width:1200px;display:flex;align-items:center;justify-content:center;gap:18px}
.brand-dot{width:74px;height:74px;border-radius:50%;border:5px solid var(--white);background:rgba(255,255,255,.12)}
.brand-name{font-size:64px;font-weight:700;color:var(--white);letter-spacing:1px}
.hero h1{position:absolute;top:315px;width:1200px;text-align:center;font-size:78px;font-weight:700;color:var(--white)}
.hero .lead{position:absolute;top:418px;width:1200px;text-align:center;font-size:20px;font-style:italic;font-weight:600;color:var(--white);line-height:30px}
.btn{display:inline-block;background:var(--blue-bright);color:var(--white);font-weight:700;font-size:20px;border-radius:30px;text-transform:uppercase;text-align:center}
.hero .btn{position:absolute;top:480px;left:460px;width:280px;height:62px;line-height:62px}
.hero-curve{position:absolute;left:0;bottom:0}

/* who */
.who{top:760px;height:560px;background:linear-gradient(180deg,#f1f3f6 0%,#fff 100%)}
.who .section-title{margin-top:0}
.who .strong{margin:40px auto 0;width:940px;text-align:center;font-size:18px;font-style:italic;font-weight:600;color:#30363d;line-height:29px}
.who .body{margin:22px auto 0;width:920px;text-align:center;font-size:15px;line-height:25px}
.seal{position:absolute;top:308px;left:512px;width:176px;height:176px;border-radius:50%;background:var(--white);box-shadow:0 4px 18px rgba(0,0,0,.18);display:flex;align-items:center;justify-content:center}
.seal span{width:118px;height:118px;border-radius:50%;border:7px solid var(--navy)}

/* services */
.services{top:1310px;height:880px}
.services .sub{margin:20px auto 0;width:800px;text-align:center;font-size:14px;font-style:italic;line-height:22px}
.grid{position:absolute;top:146px;left:35px;display:grid;grid-template-columns:550px 550px;gap:32px 30px}
.card{position:relative;height:292px}
.card .photo{position:absolute;inset:0}
.card .tag{position:absolute;left:0;bottom:0;height:48px;line-height:48px;padding:0 60px 0 22px;background:var(--blue);color:var(--white);font-size:17px;font-weight:600;clip-path:polygon(0 0,86% 0,100% 100%,0 100%)}
.divider{position:absolute;left:0;width:1200px;height:2px;background:var(--line)}
.divider-btn{position:absolute;left:490px;width:220px;height:58px;border:2px solid var(--line);border-radius:30px;background:var(--white);text-align:center;line-height:54px;font-size:19px;font-weight:700;color:var(--blue);text-transform:uppercase}
.divider-btn.title{text-transform:none}

/* testimonials */
.clients{top:2195px;height:390px}
.quotes{position:absolute;top:100px;left:125px;display:grid;grid-template-columns:290px 290px 290px;gap:60px}
.quote-mark{width:76px;height:76px;border-radius:50%;background:var(--navy);color:var(--white);font-size:64px;font-weight:800;line-height:100px;text-align:center}
.quote p{margin-top:26px;font-size:14px;line-height:23px}
.quote .who-name{margin-top:14px;font-size:17px;font-weight:700;color:var(--blue)}
.quote .who-name::before{content:"";display:inline-block;width:22px;height:2px;background:var(--blue);vertical-align:middle;margin-right:12px}

/* how it works */
.works{top:2600px;height:650px}
.works .band{position:absolute;top:0;left:0;width:1200px;height:540px;background:linear-gradient(135deg,#1f78c0 0%,#4aa6e0 45%,#2a86cc 100%)}
.works .panel{position:absolute;top:260px;left:77px;width:1046px;height:380px;background:var(--navy);padding:48px 80px 0;color:#dfe7f1;text-align:center}
.works .section-title{color:var(--white)}
.works .title-dot{border-color:var(--white)}
.works .panel p{font-size:14px;line-height:24px;margin-top:26px}
.works .panel p + p{margin-top:14px}

/* cost */
.cost{top:3300px;height:140px}
.cost h2{position:absolute;left:77px;top:0;font-size:38px;font-weight:700;color:var(--ink);line-height:48px}
.cost h2 .title-dot{display:inline-block;vertical-align:-4px;margin-right:12px}
.cost h2 .accent{display:block;padding-left:46px;color:var(--blue);font-weight:500}
.cost p{position:absolute;left:455px;top:8px;width:670px;font-size:15px;font-style:italic;line-height:25px}

/* contact */
.contact{top:3490px;height:360px}
.contact .section-title{position:absolute;top:100px;width:1200px}
.contact .sub{position:absolute;top:160px;width:1200px;text-align:center;font-size:15px;font-style:italic;color:var(--muted)}
.form{position:absolute;top:210px;left:135px;display:grid;grid-template-columns:300px 300px 300px;gap:22px 30px}
.field{height:48px;background:var(--field);border-radius:5px;padding-left:16px;line-height:48px;font-size:13px;color:var(--muted)}
.form .btn{height:48px;line-height:48px;border-radius:25px}

/* team */
.team{top:3880px;height:490px;background:linear-gradient(160deg,#f3f4f6 0%,#e4e7eb 55%,#f1f2f4 100%)}
.team .section-title{position:absolute;top:58px;width:1200px}
.avatar{position:absolute;top:160px;left:125px;width:262px;height:262px;border-radius:50%;background:radial-gradient(circle at 50% 40%,#b9c6d4 0%,#6f8297 55%,#2e3b4b 100%);border:6px solid var(--white)}
.member{position:absolute;top:168px;left:430px;width:680px}
.member h3{font-size:24px;font-weight:600;color:#2a2f36}
.member .role{font-size:14px;color:var(--blue);margin-top:6px}
.member p{font-size:14px;line-height:23px;margin-top:12px}
.socials{display:flex;gap:14px;margin-top:22px}
.socials span{width:40px;height:40px;border-radius:50%;border:2px solid var(--blue)}
.pager{position:absolute;right:28px;top:165px;display:flex;flex-direction:column;gap:16px}
.pager span{width:16px;height:16px;border-radius:50%;border:2px solid var(--blue)}
.pager span.on{background:var(--blue)}

/* subscribe */
.subscribe{top:4400px;height:380px;text-align:center}
.subscribe .section-title{margin-top:40px}
.subscribe .sub{margin:20px auto 0;width:560px;font-size:16px;font-style:italic;line-height:26px}
.sub-field{position:relative;margin:22px auto 0;width:520px;height:48px;border:1px solid #d5d9de;border-radius:25px;text-align:left;padding-left:22px;line-height:46px;font-size:13px;color:var(--muted)}
.sub-field + .sub-field{margin-top:14px}
.sub-field span{position:absolute;right:6px;top:6px;width:34px;height:34px;border-radius:50%;background:var(--navy)}
.subscribe .btn{margin-top:26px;width:250px;height:52px;line-height:52px}

/* footer */
.footer{top:4800px;height:448px;background:linear-gradient(180deg,#1b4a82 0%,#14325a 100%);overflow:hidden}
.footer-curve{position:absolute;top:0;left:0}
.footer .brand{top:90px}
.footer .brand-dot{width:56px;height:56px;border-width:4px}
.footer .brand-name{font-size:46px}
.footer .socials{position:absolute;top:212px;left:518px;gap:18px;margin:0}
.footer .socials span{width:50px;height:50px;border-color:var(--white)}
.footer nav{position:absolute;top:305px;width:1200px;display:flex;justify-content:center;gap:46px;font-size:14px;color:#dce6f2}
.footer .copy{position:absolute;top:340px;width:1200px;text-align:center;font-size:13px;color:var(--blue-bright)}
</style>
</head>
<body>

<header class="section hero">
  <div class="menu"><span></span><span></span><span></span></div>
  <div class="brand"><span class="brand-dot"></span><span class="brand-name">CoinLantern</span></div>
  <h1>The Token Sale Experts</h1>
  <p class="lead">Our experts will ensure that your ICO is run properly, communicated well, and<br>achieves your desired outcomes.</p>
  <a class="btn">Join Us Today</a>
  <svg class="hero-curve" width="1200" height="120" viewBox="0 0 1200 120" aria-hidden="true">
    <path d="M0 40 Q600 150 1200 40 L1200 120 L0 120Z" fill="#f1f3f6"/>
    <path d="M0 30 Q600 140 1200 30" fill="none" stroke="#21a9e8" stroke-width="6"/>
  </svg>
</header>

<section class="section who">
  <h2 class="section-title"><span class="title-dot"></span>Who <span class="accent">We Are ?</span></h2>
  <p class="strong">CoinLantern is the premier marketing agency for ICO's. Our experts will ensure that your ICO is run properly, communicated well, and achieves your desired outcomes.</p>
  <p class="body">We are a group of global experts connected through a cutting edge Decentralized Organizational structure powered by Smart Contracts. We have no employees – just owners. That is why your success is our shared mission.</p>
  <div class="seal"><span></span></div>
</section>

<section class="section services">
  <h2 class="section-title"><span class="title-dot"></span>What <span class="accent">We Do ?</span></h2>
  <p class="sub">Lorem Ipsum is simply dummy text of the printing and typesetting industry. Lorem Ipsum has been the industry's standard dummy text ever since the 1500s, when an unknown printer took a galley.</p>
  <div class="grid">
    <div class="card"><div class="photo" role="img" aria-label="Photo of a modern meeting room with a long table" style="background:linear-gradient(135deg,#cfe0ef,#5c86ad 60%,#1e3e60)"></div><div class="tag">Whitepaper Consultation &amp; Review</div></div>
    <div class="card"><div class="photo" role="img" aria-label="Photo of a laptop on a desk with a magnifier icon" style="background:linear-gradient(135deg,#7f9cb8,#3c5f85 55%,#1b3656)"></div><div class="tag">Secure Token Launch Website</div></div>
    <div class="card"><div class="photo" role="img" aria-label="Illustration of glowing currency icons over a hand" style="background:linear-gradient(135deg,#c9dff1,#4f8fc9 55%,#153f70)"></div><div class="tag">Marketing Representation</div></div>
    <div class="card"><div class="photo" role="img" aria-label="Photo of a presenter at a whiteboard with social media icons" style="background:linear-gradient(135deg,#f4f5f7,#c9d1da 55%,#5d6d80)"></div><div class="tag">Social Media Management</div></div>
  </div>
  <div class="divider" style="top:816px"></div>
  <div class="divider-btn" style="top:788px">View All</div>
</section>

<section class="section clients">
  <h2 class="section-title"><span class="title-dot"></span>What Our <span class="accent">Client Say</span></h2>
  <div class="quotes">
    <div class="quote"><div class="quote-mark">“</div><p>Lorem Ipsum is simply dummy text of the printing and typesetting industry. Lorem Ipsum has been the industry's standard dummy text ever since the 1500s, when an unknown printer took a galley.</p><div class="who-name">Client Name</div></div>
    <div class="quote"><div class="quote-mark">“</div><p>Lorem Ipsum is simply dummy text of the printing and typesetting industry. Lorem Ipsum has been the industry's standard dummy text ever since the 1500s, when an unknown printer took a galley.</p><div class="who-name">Client Name</div></div>
    <div class="quote"><div class="quote-mark">“</div><p>Lorem Ipsum is simply dummy text of the printing and typesetting industry. Lorem Ipsum has been the industry's standard dummy text ever since the 1500s, when an unknown printer took a galley.</p><div class="who-name">Client Name</div></div>
  </div>
</section>

<section class="section works">
  <div class="band" role="img" aria-label="Blue toned photo of hands working on a laptop and phone"></div>
  <div class="panel">
    <h2 class="section-title"><span class="title-dot"></span>How Does <span class="accent">It Work?</span></h2>
    <p>Our tight-knit group of experts becomes a part of your team for the crucial period leading up to and during your ICO. We take the time to thoroughly understand your project and the people behind it. By drawing on our deep expertise in the space and network of valuable connections, we work closely with you to develop and implement the steps involved in executing a successful ICO. Best practices, market conditions, and investor psychology are constantly changing. We stay laser-focused on the ICO segment of the cryptocurrency landscape to stay up to date.</p>
    <p>Bringing CoinLantern in to run your sale allows your team members to focus on execution. Without the hassle, distraction, and frustration of trying to do it yourself, you have more bandwidth to build out your vision.</p>
  </div>
</section>

<section class="section cost">
  <h2><span class="title-dot"></span>How Much <span class="accent">Does It Cost?</span></h2>
  <p>Every Token sale is unique, that is why CoinLantern begins with a one-on-one conversation to identify your specific needs and agree upon terms that make sense for all parties. We structure engagements according to the principle of aligned interests – our success is your success and vice versa.</p>
</section>

<section class="section contact">
  <div class="divider" style="top:20px"></div>
  <div class="divider-btn" style="top:-8px">Contact Us</div>
  <h2 class="section-title"><span class="title-dot"></span>How Do I <span class="accent">Get Started?</span></h2>
  <p class="sub">Need a free quote, or have a question? Get in touch!</p>
  <div class="form">
    <div class="field">Name*</div><div class="field">Email*</div><div class="field">Phone*</div>
    <div class="field">Company Name*</div><div class="field">Message*</div><a class="btn">Submit</a>
  </div>
</section>

<section class="section team">
  <h2 class="section-title"><span class="title-dot"></span>Meet <span class="accent">Our Team</span></h2>
  <div class="avatar" role="img" aria-label="Portrait photo of a team member"></div>
  <div class="member">
    <h3>Marius Eldenbrook</h3>
    <div class="role">CoinLantern</div>
    <p>Lorem Ipsum is simply dummy text of the printing and typesetting industry. Lorem Ipsum has been the industry's standard dummy text ever since the 1500s, when an unknown printer took a galley. Lorem Ipsum is simply dummy text of the printing and typesetting industry. Lorem Ipsum has been the industry's standard dummy text ever since the.</p>
    <div class="socials"><span></span><span></span><span></span></div>
  </div>
  <div class="pager"><span></span><span></span><span></span><span></span><span class="on"></span><span></span></div>
</section>

<section class="section subscribe">
  <h2 class="section-title"><span class="title-dot"></span>Subscribe To <span class="accent">Our Mailing List</span></h2>
  <p class="sub">Would you like to receive exclusive access to articles, white papers &amp; our regular monthly newsletter?</p>
  <div class="sub-field">Enter Name*<span></span></div>
  <div class="sub-field">Enter Email*<span></span></div>
  <a class="btn">Subscribe</a>
</section>

<footer class="section footer">
  <svg class="footer-curve" width="1200" height="80" viewBox="0 0 1200 80" aria-hidden="true">
    <path d="M0 0 L1200 0 L1200 30 Q600 -30 0 30Z" fill="#ffffff"/>
    <path d="M0 34 Q600 -26 1200 34" fill="none" stroke="#21a9e8" stroke-width="6"/>
  </svg>
  <div class="brand"><span class="brand-dot"></span><span class="brand-name">CoinLantern</span></div>
  <div class="socials"><span></span><span></span><span></span></div>
  <nav><span>Home</span><span>Who We Are</span><span>What We Do</span><span>Testimonials</span><span>Team</span><span>Contact Us</span></nav>
  <p class="copy">© CoinLantern 2017. All Rights Reserved.</p>
</footer>

</body>
</html>
```